R&K Security Services PTY. LTD.

Ive just had my logo made and I'm looking for some simple but strong designs for my business cards the company is a security company.

Please use dark colors.

Regards,

Dale Prentiss

Reason: Need more time for discussion with other directors

Industry/Entity Type

Security

Font styles to use
Sans Serif
Decorative

```html
<!DOCTYPE html>
<html lang="en">
<head>
<meta charset="utf-8">
<title>R&amp;K Security Services – Business Card</title>
<link rel="stylesheet" href="https://fonts.googleapis.com/css2?family=Cinzel:wght@400;600&family=Questrial&display=swap">
<style>
  :root {
    --teal-bright: #0e6384;
    --teal-mid: #07425a;
    --teal-deep: #03202c;
    --ink-band: rgba(2, 20, 30, 0.55);
    --panel: rgba(3, 22, 32, 0.72);
    --text-light: #f2f4f5;
    --text-grey: #9a9c9e;
    --icon-grey: #8d8f91;
    --motto-grey: #8e9294;
  }
  html, body {
    margin: 0;
    padding: 0;
    width: 1200px;
    height: 720px;
    overflow: hidden;
    background: #0d1114;
  }
  .card {
    position: relative;
    width: 1200px;
    height: 720px;
    overflow: hidden;
    font-family: "Questrial", Arial, sans-serif;
    color: var(--text-light);
    background:
      repeating-linear-gradient(180deg, rgba(255,255,255,0.025) 0 1px, transparent 1px 4px),
      radial-gradient(ellipse 80% 70% at 25% 5%, var(--teal-bright) 0%, var(--teal-mid) 45%, var(--teal-deep) 100%);
  }
  .brand-mark {
    position: absolute;
    left: 64px;
    top: 110px;
    width: 200px;
    display: flex;
    flex-direction: column;
    align-items: center;
    gap: 14px;
  }
  .brand-mark__dot {
    width: 40px;
    height: 40px;
    border-radius: 50%;
    background: var(--text-grey);
  }
  .brand-mark__name {
    font-size: 54px;
    color: var(--text-grey);
    letter-spacing: 2px;
    line-height: 1;
  }
  .identity-band {
    position: absolute;
    left: 245px;
    top: 130px;
    width: 955px;
    height: 117px;
    background: linear-gradient(90deg, var(--ink-band) 0%, rgba(2,20,30,0.45) 60%, rgba(2,20,30,0.25) 100%);
  }
  .person-name {
    position: absolute;
    left: 285px;
    top: 138px;
    margin: 0;
    font-weight: 400;
    font-size: 44px;
    letter-spacing: 4px;
    line-height: 1;
    color: var(--text-light);
  }
  .person-name__surname { color: var(--text-grey); }
  .postal-address {
    position: absolute;
    left: 285px;
    top: 190px;
    margin: 0;
    font-size: 33px;
    line-height: 1;
    font-style: normal;
  }
  .contact-row {
    position: absolute;
    display: flex;
    align-items: center;
    font-size: 36px;
    line-height: 1;
  }
  .contact-row svg { fill: var(--icon-grey); flex: none; }
  .contact-row--phones { left: 275px; top: 282px; }
  .contact-row--email { left: 266px; top: 388px; }
  .contact-row--web { left: 272px; top: 475px; }
  .phone-item { display: flex; align-items: center; }
  .phone-item + .phone-item { margin-left: 52px; }
  .icon-gap { margin-right: 30px; }
  .divider { margin: 0 24px; }
  .motto-strip {
    position: absolute;
    left: 0;
    top: 600px;
    width: 1200px;
    height: 120px;
  }
  .motto {
    position: absolute;
    top: 0;
    height: 120px;
    background: var(--panel);
    display: flex;
    align-items: flex-start;
    justify-content: center;
    padding-top: 23px;
    box-sizing: border-box;
    font-family: "Cinzel", "Times New Roman", serif;
    font-weight: 600;
    font-size: 24px;
    letter-spacing: 4px;
    color: var(--motto-grey);
  }
  .motto--integritas { left: 0; width: 395px; }
  .motto--fortitudo { left: 421px; width: 356px; }
  .motto--intelligentia { left: 802px; width: 398px; }
</style>
</head>
<body>
<main class="card">
  <div class="brand-mark">
    <span class="brand-mark__dot"></span>
    <span class="brand-mark__name">R&amp;K</span>
  </div>

  <div class="identity-band"></div>
  <h1 class="person-name">DALE<span class="person-name__surname">PRENTISS</span></h1>
  <address class="postal-address">P.O. Box 7 Ashvale Victoria 3152</address>

  <div class="contact-row contact-row--phones">
    <span class="phone-item">
      <svg class="icon-gap" width="30" height="52" viewBox="0 0 30 52" aria-hidden="true">
        <path d="M5 0h20a5 5 0 0 1 5 5v42a5 5 0 0 1-5 5H5a5 5 0 0 1-5-5V5a5 5 0 0 1 5-5zm-1 7v34h22V7zm11 37a3 3 0 1 0 0 6 3 3 0 0 0 0-6z"/>
      </svg>
      0412555019
    </span>
    <span class="phone-item">
      <svg class="icon-gap" width="42" height="42" viewBox="0 0 24 24" aria-hidden="true">
        <path d="M6.6 10.8a15.1 15.1 0 0 0 6.6 6.6l2.2-2.2a1 1 0 0 1 1-.25 11.4 11.4 0 0 0 3.6.57 1 1 0 0 1 1 1V20a1 1 0 0 1-1 1A17 17 0 0 1 3 4a1 1 0 0 1 1-1h3.5a1 1 0 0 1 1 1c0 1.25.2 2.45.57 3.57a1 1 0 0 1-.25 1z"/>
      </svg>
      (03) 95550187
    </span>
  </div>

  <div class="contact-row contact-row--email">
    <svg class="icon-gap" width="50" height="34" viewBox="0 0 50 34" aria-hidden="true">
      <path d="M0 0h50v34H0z" opacity="0.9"/>
      <path d="M2 2l23 18L48 2" fill="none" stroke="#0a3548" stroke-width="2.5"/>
    </svg>
    R.K@prentiss.net.au<span class="divider">|</span>dale@prentiss.net.au
  </div>

  <div class="contact-row contact-row--web">
    <svg class="icon-gap" width="38" height="38" viewBox="0 0 38 38" aria-hidden="true">
      <g fill="none" stroke="var(--icon-grey)" stroke-width="2.4">
        <circle cx="19" cy="19" r="17"/>
        <ellipse cx="19" cy="19" rx="7.5" ry="17"/>
        <path d="M2 19h34M5 10h28M5 28h28M19 2v34"/>
      </g>
    </svg>
    www.prentiss.net.au
  </div>

  <div class="motto-strip">
    <div class="motto motto--integritas">INTEGRITAS</div>
    <div class="motto motto--fortitudo">FORTITUDO</div>
    <div class="motto motto--intelligentia">INTELLIGENTIA</div>
  </div>
</main>
</body>
</html>
```